Lumacraftery 'Quiet Harbour' Book Cover Design project

I need to revise the book cover design I have for my coming book. The design I created through PixelGuild is great but the book has grown and changed so I'm looking for an alternative/option design. I can then choose later from the different options.

I need a book cover that represents the unique book I am creating.

Book Title:
The Open Meadow

Subtitle: Walking Forward Beyond Every Box

The book is targeting all readers with a special focus on same sex attracted readers. It should not have stereotypical images.

I am including a file of the book cover I have had designed. The back cover blurb, author info and author pic will remain the same. The colouring of the back cover and spine will, of course, change to match the colouring of the front cover.

The new title will be on the spine and the new title wording.

The front cover will be markedly different using the bold images and rainbow colours of the images found in the files I am uploading for you.

I am thinking of a large boldly coloured rainbow face with the title and subtitle ON the image. The image will be the whole cover. It will fill the cover as much as possible with the text added onto the pic.

The bold pictures I am including will give you the idea of what I'm looking for.

ANY of the images I've uploaded can be used as the actual front cover image OR the designer might have/find some suitable image to be used. The image is to be large and bold and fill the cover. Hopefully a positive energy.
It needs to be eye-catching and striking and bold and positive.

So...the book cover sample file I've provided can keep the back cover with completely new colouring. The front cover is completely new with new image, wording and energy.

It is to be a rainbow coloured face or figure for the cover image.

I hope that is clear enough for you. I'm very happy to discuss and clarify these ideas with the designer. Looking forward to another great PixelGuild experience.

Target Market(s)

Wide audience with special focus on Same Sex Attracted individuals

Font styles to use
Script
Other font styles liked:
• Some form of handwriting font to make the book title and text appear more personal....as if handwritten by me.

Requirements
Must have
• Boldness, Quirky, Rainbow Colour, Image to fill the cover, maybe dark cover contrasting background.
Nice to have
• A well balanced back cover especially in the area where the barcode will be placed.
Should not have
• No stereotypical images

```html
<!DOCTYPE html>
<html lang="en">
<head>
<meta charset="utf-8">
<title>The Open Meadow – Cover and Spine</title>
<link rel="stylesheet" href="https://fonts.googleapis.com/css2?family=Great+Vibes&family=Encode+Sans:wght@300;400&display=swap">
<style>
  :root {
    --backdrop: #ffffff;
    --cover-dark: #0b0a0c;
    --tone-pink: #e0338f;
    --tone-teal: #2fa7b8;
    --tone-green: #6f9a3a;
    --tone-gold: #c8923a;
    --tone-violet: #6b3d8f;
    --subtitle-pink: #ee3f9c;
    --title-white: #ffffff;
    --author-white: #f2f2f2;
    --spine-edge: rgba(0, 0, 0, 0.35);
  }
  * { box-sizing: border-box; margin: 0; padding: 0; }
  html, body {
    width: 1200px;
    height: 1200px;
    overflow: hidden;
    background: var(--backdrop);
  }
  .canvas {
    position: relative;
    width: 1200px;
    height: 1200px;
  }

  /* Spine */
  .book-spine {
    position: absolute;
    left: 215px;
    top: 70px;
    width: 70px;
    height: 1060px;
    overflow: hidden;
    background: var(--cover-dark);
    box-shadow: inset -6px 0 8px var(--spine-edge);
  }
  .spine-photo {
    position: absolute;
    inset: 0;
    background: linear-gradient(180deg,
      #3a2a2e 0%,
      var(--tone-pink) 22%,
      var(--tone-teal) 40%,
      var(--tone-gold) 58%,
      var(--tone-green) 72%,
      var(--tone-pink) 86%,
      #2a2226 100%);
  }
  .spine-title {
    position: absolute;
    left: 0;
    top: 40px;
    width: 70px;
    height: 600px;
    writing-mode: vertical-rl;
    text-align: start;
    font-family: "Great Vibes", cursive;
    font-weight: 400;
    font-size: 48px;
    line-height: 70px;
    color: var(--title-white);
    white-space: nowrap;
  }
  .spine-author {
    position: absolute;
    left: 0;
    top: 720px;
    width: 70px;
    height: 300px;
    writing-mode: vertical-rl;
    font-family: "Encode Sans", sans-serif;
    font-weight: 400;
    font-size: 24px;
    line-height: 70px;
    letter-spacing: 2px;
    text-transform: uppercase;
    color: var(--author-white);
    white-space: nowrap;
  }

  /* Front cover */
  .book-cover {
    position: absolute;
    left: 285px;
    top: 70px;
    width: 700px;
    height: 1060px;
    overflow: hidden;
    background: var(--cover-dark);
  }
  .cover-photo {
    position: absolute;
    inset: 0;
    background: linear-gradient(100deg,
      var(--tone-violet) 0%,
      var(--tone-pink) 18%,
      var(--tone-teal) 34%,
      var(--tone-gold) 48%,
      var(--tone-green) 60%,
      #2a2226 76%,
      var(--cover-dark) 92%);
  }
  .subtitle {
    position: absolute;
    left: 420px;
    top: 240px;
    width: 170px;
    text-align: center;
    font-family: "Encode Sans", sans-serif;
    font-weight: 400;
    font-size: 28px;
    line-height: 1.3;
    color: var(--subtitle-pink);
  }
  .title {
    position: absolute;
    left: 0;
    top: 470px;
    width: 700px;
    height: 360px;
    font-family: "Great Vibes", cursive;
    font-weight: 400;
    color: var(--title-white);
    line-height: 1;
  }
  .title-line { display: block; position: absolute; white-space: nowrap; }
  .title-line--first { left: 120px; top: 0; font-size: 150px; }
  .title-line--second { left: 150px; top: 170px; font-size: 150px; }
  .author {
    position: absolute;
    left: 0;
    top: 935px;
    width: 700px;
    text-align: center;
    padding-left: 60px;
    font-family: "Encode Sans", sans-serif;
    font-weight: 400;
    font-size: 34px;
    letter-spacing: 2px;
    color: var(--author-white);
    text-transform: uppercase;
  }
</style>
</head>
<body>
  <main class="canvas">
    <section class="book-spine">
      <div class="spine-photo" role="img" aria-label="Continuation of the rainbow body-paint photograph wrapping onto the spine"></div>
      <p class="spine-title">The Open Meadow</p>
      <p class="spine-author">Dane Holloway</p>
    </section>
    <section class="book-cover">
      <div class="cover-photo" role="img" aria-label="Full-bleed photograph of a figure covered in bold rainbow body paint against a dark background"></div>
      <p class="subtitle">Walking Forward Beyond Every Box</p>
      <h1 class="title">
        <span class="title-line title-line--first">The Open</span>
        <span class="title-line title-line--second">Meadow</span>
      </h1>
      <p class="author">Dane Holloway</p>
    </section>
  </main>
</body>
</html>
```